We sell companies excess stock for them

We need a business card for a company based in New Zealand called 'StockHarbor'.

Check out our website to get an idea www.stockharbor.example

We help other businesses to;
- Sell Excess Stock
- Manage Product Returns
- Sell Company Assets

Our logo is attached for your reference
The font used is 'RifficFree-Bold'

Target Market(s)

Businesses

Industry/Entity Type

Business

Contact Information for Business Card

Name: Mark Pellow
Phone: 027 846 2093
email: markpellow@stockharbor.example
website: www.stockharbor.example

Font styles to use
Other font styles liked:
• Unsure

Colors
9bcb3b

Requirements
Must have
• coming soon
Nice to have
• coming soon
Should not have
• coming soon

```html
<!DOCTYPE html>
<html lang="en">
<head>
<meta charset="utf-8">
<title>StockHarbor Business Card</title>
<link rel="stylesheet" href="https://fonts.googleapis.com/css2?family=Fredoka:wght@600;700&family=Lato:wght@400&display=swap">
<style>
  :root {
    --brand-green: #9bcb3b;
    --brand-green-dark: #7fb02a;
    --ink: #231f20;
    --band: #221e1f;
    --paper: #ffffff;
    --backdrop: #1c1c1c;
  }
  * { margin: 0; padding: 0; box-sizing: border-box; }
  html, body {
    width: 1189px; height: 1200px; overflow: hidden;
    background: var(--backdrop);
  }
  .sheet { position: relative; width: 1189px; height: 1200px; }
  .card {
    position: absolute; left: 166px; width: 857px; height: 490px;
    border-radius: 30px; overflow: hidden;
  }
  .card--front { top: 75px; background: var(--brand-green); }
  .card--back { top: 635px; background: var(--paper); }
  .card__band { position: absolute; left: 0; top: 0; width: 100%; height: 100%; z-index: 2; }
  .mascot {
    position: absolute; z-index: 1; border-radius: 50%;
    background: radial-gradient(ellipse at 50% 45%, #f3c070 0%, #b9dc6a 45%, rgba(155,203,59,0.45) 72%, rgba(155,203,59,0) 100%);
  }
  .card--front .mascot { left: 230px; top: 24px; width: 390px; height: 400px; }
  .card--back .mascot { left: 478px; top: 26px; width: 350px; height: 400px; }
  .brand-name {
    position: absolute; left: 44px; top: 44px; z-index: 3;
    font-family: "Fredoka", sans-serif; font-weight: 700;
    font-size: 60px; line-height: 1; letter-spacing: -1px; color: var(--ink);
  }
  .person {
    position: absolute; left: 44px; top: 183px; z-index: 3;
    font-family: "Fredoka", sans-serif; font-weight: 700;
    font-size: 34px; line-height: 1; color: var(--ink);
  }
  .person__last { color: var(--brand-green); }
  .contact-list { position: absolute; left: 44px; top: 230px; list-style: none; z-index: 3; }
  .contact-list li {
    display: flex; align-items: center; height: 28.5px;
    font-family: "Lato", sans-serif; font-size: 20px; color: var(--ink);
  }
  .contact-list svg { width: 26px; height: 26px; margin-right: 8px; flex: none; }
  .tagline {
    position: absolute; left: 44px; top: 338px; z-index: 3;
    font-family: "Fredoka", sans-serif; font-weight: 700;
    font-size: 28px; line-height: 1; color: var(--brand-green);
  }
  .services {
    position: absolute; left: 44px; top: 381px; z-index: 3;
    font-family: "Lato", sans-serif; font-size: 20px; line-height: 27px; color: var(--ink);
  }
  .services__sep { color: var(--brand-green); }
</style>
</head>
<body>
<main class="sheet">
  <section class="card card--front">
    <div class="mascot" role="img" aria-label="Cartoon delivery mascot in green cap and overalls running with an orange parcel, giving a thumbs up, over a faint repeated brand-name pattern"></div>
    <svg class="card__band" viewBox="0 0 857 490" preserveAspectRatio="none" aria-hidden="true">
      <path d="M0 424 L350 458 L857 420 L857 490 L0 490 Z" fill="var(--band)"/>
    </svg>
  </section>

  <section class="card card--back">
    <div class="mascot" role="img" aria-label="Cartoon delivery mascot in green cap and overalls running with an orange parcel, giving a thumbs up"></div>
    <svg class="card__band" viewBox="0 0 857 490" preserveAspectRatio="none" aria-hidden="true">
      <path d="M0 444 L190 470 L857 428 L857 490 L0 490 Z" fill="var(--band)"/>
    </svg>

    <div class="brand-name">StockHarbor</div>
    <div class="person">Mark <span class="person__last">Pellow</span></div>

    <ul class="contact-list">
      <li>
        <svg viewBox="0 0 26 26" aria-hidden="true"><circle cx="13" cy="13" r="11.5" fill="none" stroke="var(--brand-green)" stroke-width="2"/><path d="M9.5 7.5c-1.2 .8-1.5 2.2-.8 4 .9 2.4 2.6 4.4 4.8 5.6 1.5.8 2.9.6 3.8-.4l-2-2c-.5.3-1 .4-1.6 0-1-.7-1.8-1.7-2.3-2.8-.2-.6 0-1.1.4-1.5z" fill="var(--brand-green)"/></svg>
        027 846 2093
      </li>
      <li>
        <svg viewBox="0 0 26 26" aria-hidden="true"><circle cx="13" cy="13" r="11.5" fill="none" stroke="var(--brand-green)" stroke-width="2"/><rect x="7" y="9" width="12" height="8.5" rx="1" fill="var(--brand-green)"/><path d="M7.5 9.5 L13 14 L18.5 9.5" fill="none" stroke="#fff" stroke-width="1.2"/></svg>
        markpellow@stockharbor.example
      </li>
      <li>
        <svg viewBox="0 0 26 26" aria-hidden="true"><circle cx="13" cy="13" r="11.5" fill="none" stroke="var(--brand-green)" stroke-width="2"/><circle cx="13" cy="13" r="6.5" fill="none" stroke="var(--brand-green)" stroke-width="1.4"/><ellipse cx="13" cy="13" rx="3" ry="6.5" fill="none" stroke="var(--brand-green)" stroke-width="1.2"/><path d="M6.5 13 H19.5 M7.5 10 H18.5 M7.5 16 H18.5" stroke="var(--brand-green)" stroke-width="1.1"/></svg>
        www.stockharbor.example
      </li>
    </ul>

    <div class="tagline">We help other businesses to</div>
    <div class="services">
      Sell Excess Stock <span class="services__sep">|</span> Manage Product Returns<br>
      Sell Company Assets
    </div>
  </section>
</main>
</body>
</html>
```